Business card

We are looking for a creative person to deigns our company business card.

Target Market(s)

College age student

Industry/Entity Type

Accommodation

Contact Information for Business Card

We want a fun, clean and sophisticated design. It should look good, but more importantly the information should be legible.

Font styles to use
Serif
Sans Serif
Other font styles liked:
• Open Sans ,

Colors
33a6d7

Requirements
Must have
• Must have a young and memorable message. Be legible.
• Our logo on the back on a solid blue , please find color and logo attached
• LodgeBridgely.net on the back.
Nice to have
• I would like to have couple of different fonts on the LodgeBridgely.net on the back of the cards with a solid blue.

```html
<!DOCTYPE html>
<html lang="en">
<head>
<meta charset="utf-8">
<title>LodgeBridgely Business Card</title>
<link href="https://fonts.googleapis.com/css2?family=Open+Sans:wght@400;600;700&family=Roboto:wght@400;500&display=swap" rel="stylesheet">
<style>
  :root {
    --bg: #e4e6e9;
    --card: #ffffff;
    --brand-blue: #3a93d6;
    --brand-navy: #17518a;
    --ink: #1e1e1e;
    --faint-blue: #e8eef9;
  }
  * { margin: 0; padding: 0; box-sizing: border-box; }
  html, body {
    width: 1200px; height: 900px; overflow: hidden;
    background: var(--bg);
    font-family: "Roboto", "Open Sans", sans-serif;
  }
  .stage {
    position: relative; width: 1200px; height: 900px;
    display: flex; flex-direction: column; align-items: center; justify-content: center; gap: 60px;
  }
  .card {
    position: relative; width: 560px; height: 320px;
    background: var(--card); border-radius: 18px;
    box-shadow: 0 6px 18px rgba(0,0,0,0.18);
    overflow: hidden;
  }
  /* Front */
  .card-front { display: flex; align-items: center; justify-content: center; }
  .front-halo {
    position: absolute; width: 220px; height: 220px; border-radius: 50%;
    background: var(--faint-blue); left: 170px; top: 50px;
  }
  .front-name {
    position: relative; font-family: "Open Sans", sans-serif; font-weight: 600;
    font-size: 46px; color: var(--brand-blue); letter-spacing: 0.5px;
  }
  /* Back */
  .brand-lockup { position: absolute; left: 44px; top: 40px; display: flex; align-items: center; gap: 12px; }
  .brand-square { width: 56px; height: 56px; background: var(--brand-blue); }
  .brand-name { font-family: "Open Sans", sans-serif; font-weight: 700; font-size: 22px; color: var(--brand-navy); }
  .divider { position: absolute; left: 40px; right: 40px; top: 170px; height: 2px; background: var(--brand-blue); }
  .person { position: absolute; right: 44px; top: 118px; text-align: right; }
  .person-name { font-size: 21px; font-weight: 500; color: var(--brand-navy); letter-spacing: 0.3px; }
  .person-name .first { color: var(--brand-blue); }
  .person-role { font-size: 10px; color: var(--ink); letter-spacing: 0.5px; }
  .address { position: absolute; right: 44px; top: 182px; text-align: right; font-size: 13px; line-height: 1.45; color: var(--ink); }
  .contacts { position: absolute; left: 44px; top: 184px; list-style: none; }
  .contacts li { display: flex; align-items: center; gap: 10px; height: 26px; font-size: 14px; color: var(--ink); }
  .contact-icon { width: 20px; height: 20px; background: var(--brand-blue); display: flex; align-items: center; justify-content: center; }
</style>
</head>
<body>
<main class="stage">
  <section class="card card-front">
    <div class="front-halo"></div>
    <div class="front-name">LodgeBridgely.net</div>
  </section>

  <section class="card card-back">
    <div class="brand-lockup">
      <div class="brand-square"></div>
      <div class="brand-name">LodgeBridgely</div>
    </div>

    <div class="person">
      <div class="person-name"><span class="first">EVAN</span> MARLOWE</div>
      <div class="person-role">OWNER</div>
    </div>
    <div class="divider"></div>
    <div class="address">2207 - 48 Harbor Rd. Suite 5<br>Portland, OR 97201</div>

    <ul class="contacts">
      <li><span class="contact-icon">
        <svg width="12" height="12" viewBox="0 0 12 12"><path d="M2 1h2.5l1 3-1.5 1a6 6 0 0 0 3 3l1-1.5 3 1V10a1 1 0 0 1-1 1A9 9 0 0 1 1 2a1 1 0 0 1 1-1z" fill="#fff"/></svg>
      </span>555-201-4378</li>
      <li><span class="contact-icon">
        <svg width="12" height="12" viewBox="0 0 12 12"><rect x="1" y="2" width="10" height="3" rx="1" fill="#fff"/><rect x="2" y="6" width="8" height="5" rx="1" fill="#fff"/></svg>
      </span>555-201-4378</li>
      <li><span class="contact-icon">
        <svg width="12" height="12" viewBox="0 0 12 12"><rect x="1" y="3" width="10" height="7" fill="none" stroke="#fff" stroke-width="1.2"/><path d="M1 3l5 4 5-4" fill="none" stroke="#fff" stroke-width="1.2"/></svg>
      </span>hello@lodgebridgely.net</li>
      <li><span class="contact-icon">
        <svg width="12" height="12" viewBox="0 0 12 12"><circle cx="6" cy="6" r="4.8" fill="none" stroke="#fff" stroke-width="1.1"/><ellipse cx="6" cy="6" rx="2" ry="4.8" fill="none" stroke="#fff" stroke-width="1"/><path d="M1.2 6h9.6" stroke="#fff" stroke-width="1"/></svg>
      </span>LodgeBridgely.net</li>
    </ul>
  </section>
</main>
</body>
</html>
```